International Flower distributer needs a landing page

We are looking to have a landing page made that will be easy to maintain and upload more content as our business grows.

We like the template designs and ease of use of Pagewright. We'd explore other host sites.

Hello,

To start we would like something that can be managed and updated on a platform like pagewright. We like page wright because of the premade designs and flexibility.

Website requirements:

- About us:

- Marlowe Vantage Corp - Established 1999

- Verna Holt - Founder

- Danielle Holt - Account Executive

- Gregory Holt - Director of Operations

- Pilar Wendham - (Jo's Job Description?)

- Renata Valcourt (Make us look like a bigger company with more staff)

What we do:

- Personalized Customer service

- Exclusively Mass market experience to meet high demands

- Dedicated team assigned to your account

How we do it:

- Partnerships with farms in COlombia, ecuador and costa rica

- Farm fresh delivered directly from cargo planes to state of the art cooler facility at Delmont Airport

- Verity Trust?

Products we Sell:

- Farm made bouquets

- Consumer Bunches

- Programs Tailored to fit customer's retail program

For more Information:

- Gregory and Danielle phone and email

- Submit email inquiry

Gathering more feedback

Corporate buyers that want to verify who we are and get our contact information

Floral, but not a flower shop. We import farm fresh cut flowers from south america and send them directly to supermarkets around the country.

• We are not selling anything on the website. We sell business to business.

```html
<!DOCTYPE html>
<html lang="en">
<head>
<meta charset="utf-8">
<title>Marlowe Vantage – International Flower Distributor</title>
<link href="https://fonts.googleapis.com/css2?family=Montserrat:wght@500;700;800&family=Arimo:wght@400;700&display=swap" rel="stylesheet">
<style>
:root{
  --navy:#2e2f95;
  --navy-deep:#28298a;
  --green:#7bc13a;
  --green-dark:#63a82a;
  --ink:#333;
  --grey:#666;
  --light:#f4f6f1;
  --white:#fff;
}
*{margin:0;padding:0;box-sizing:border-box}
html,body{width:1200px;height:4866px;overflow:hidden}
body{position:relative;font-family:"Arimo",Arial,sans-serif;color:var(--ink);background:var(--white)}
.abs{position:absolute}
.btn{position:absolute;background:var(--green);color:var(--white);font-size:15px;display:flex;align-items:center;justify-content:center;border-radius:2px}
.section-title{position:absolute;left:0;width:1200px;text-align:center;font-family:"Arimo",Arial,sans-serif;font-weight:700;font-size:33px;color:var(--navy)}
.divider{position:absolute;left:518px;width:164px;height:24px}
.divider::before,.divider::after{content:"";position:absolute;top:11px;width:62px;height:1px;background:#c8c8d8}
.divider::before{left:0}.divider::after{right:0}
.divider span{position:absolute;left:72px;top:2px;width:20px;height:20px;border:2px solid #aab;transform:rotate(45deg)}
.photo{position:absolute}
/* hero */
.hero{position:absolute;left:0;top:0;width:1200px;height:694px;background:linear-gradient(180deg,#9fb58a 0%,#6f8f4f 35%,#4a5a2e 65%,#2a1c14 100%)}
.brand{position:absolute;left:165px;top:20px;display:flex;align-items:center;gap:12px}
.brand-mark{width:60px;height:60px;border-radius:50%;background:var(--navy)}
.brand-name{font-family:"Montserrat",sans-serif;font-weight:800;font-size:22px;line-height:24px;color:var(--navy)}
.topbar{position:absolute;right:162px;top:24px;display:flex;gap:20px;font-size:14px;color:var(--navy)}
.topbar div{display:flex;align-items:center;gap:10px}
.topbar svg{width:22px;height:22px}
.nav{position:absolute;right:162px;top:66px;display:flex;gap:26px;font-size:14px;color:var(--navy)}
.nav .active{color:var(--green);font-weight:700}
.hero h1{position:absolute;left:0;top:420px;width:1200px;text-align:center;font-family:"Montserrat",sans-serif;font-weight:800;font-size:58px;line-height:62px;color:var(--white)}
.hero p{position:absolute;left:0;top:556px;width:1200px;text-align:center;font-family:"Montserrat",sans-serif;font-weight:500;font-size:19px;color:var(--white)}
/* about */
.team-thumb{position:absolute;top:848px;width:145px;height:145px}
.founder-name{position:absolute;left:163px;top:1075px;font-size:22px;font-weight:700;color:var(--navy)}
.founder-name small{font-size:13px;font-weight:400;color:var(--green)}
.lead{position:absolute;font-size:15px;line-height:26px;color:#333}
.body-copy{position:absolute;font-size:12.5px;line-height:23px;color:#666;text-align:justify}
.socials{position:absolute;display:flex;gap:14px}
.socials i{display:block;width:12px;height:12px;border-radius:50%;background:var(--navy)}
.frame-green{position:absolute;background:var(--green)}
.frame-navy{position:absolute;background:var(--navy)}
/* what we do */
.what-band{position:absolute;left:0;top:1467px;width:1200px;height:368px;background:linear-gradient(120deg,#3a3ca8,#3436a0 50%,#4a4cb4)}
.what-card{position:absolute;top:1642px;width:266px;height:268px}
.what-caption{position:absolute;top:1872px;width:228px;height:76px;background:var(--white);box-shadow:0 3px 10px rgba(0,0,0,.12);font-size:15px;line-height:20px;color:#444;display:flex;align-items:center;justify-content:center;text-align:center}
/* how */
.how-icon{position:absolute;top:2118px;width:100px;height:100px;border-radius:50%;background:#eef5e6}
.how-icon svg{position:absolute;left:20px;top:20px;width:60px;height:60px}
.how-text{position:absolute;top:2233px;width:220px;text-align:center;font-size:14.5px;line-height:20px;color:#444}
.how-arrow{position:absolute;top:2140px;width:140px;height:40px}
/* banner */
.banner{position:absolute;left:160px;top:2452px;width:880px;height:338px;border-radius:8px;background:linear-gradient(90deg,#eef2e2,#e6ecd4 50%,#edf1df)}
.banner h2{position:absolute;left:0;top:60px;width:880px;text-align:center;font-size:29px;line-height:37px;color:var(--navy);font-weight:700}
.banner p{position:absolute;left:50px;top:144px;width:780px;text-align:center;font-size:13px;line-height:23px;color:#666}
/* products */
.products{position:absolute;left:0;top:2865px;width:1200px;height:1345px;background:linear-gradient(180deg,#7dc33c 0%,#74bb34 40%,#6aae2e 70%,#5f9f28 100%)}
.products .section-title{color:var(--white)}
.prod-title{position:absolute;font-size:22px;line-height:26px;font-weight:700;color:var(--white)}
.products .lead,.products .body-copy{color:var(--white)}
.products .body-copy{opacity:.9}
/* info */
.contact-name{position:absolute;font-size:23px;font-weight:700;color:#333}
.contact-role{position:absolute;font-size:14px;color:#555}
.contact-row{position:absolute;display:flex;align-items:center;gap:14px;font-size:13px;color:#555;line-height:22px}
.contact-row.right{text-align:right}
.dot{width:36px;height:36px;border-radius:50%;background:var(--green);flex:none;display:flex;align-items:center;justify-content:center}
.dot svg{width:18px;height:18px}
/* footer */
.footer{position:absolute;left:0;top:4745px;width:1200px;height:121px;background:var(--navy-deep)}
.footer p{position:absolute;left:0;top:28px;width:1200px;text-align:center;font-size:12.5px;color:var(--white)}
.footer .socials{left:541px;top:66px;gap:8px}
.footer .socials i{width:34px;height:34px;background:var(--green);border:2px solid var(--white)}
</style>
</head>
<body>

<header class="hero">
  <div class="photo" role="img" aria-label="Farm workers tending a field of cut flowers, one holding a tablet" style="inset:0;background:linear-gradient(180deg,rgba(150,175,120,.5),rgba(60,80,40,.2) 50%,rgba(40,20,15,.6))"></div>
  <div class="brand"><div class="brand-mark"></div><div class="brand-name">MARLOWE<br>VANTAGE</div></div>
  <div class="topbar">
    <div><svg viewBox="0 0 22 22"><rect x="1" y="1" width="20" height="20" fill="none" stroke="#2e2f95" stroke-width="1.5"/><path d="M7 6l2 0 1 3-1.5 1a7 7 0 0 0 3.5 3.5L13 12l3 1v2a1 1 0 0 1-1 1A10 10 0 0 1 6 7a1 1 0 0 1 1-1z" fill="#2e2f95"/></svg>555-310-4420</div>
    <div><svg viewBox="0 0 22 22"><rect x="1" y="1" width="20" height="20" fill="none" stroke="#2e2f95" stroke-width="1.5"/><path d="M11 5a4 4 0 0 1 4 4c0 3-4 8-4 8s-4-5-4-8a4 4 0 0 1 4-4z" fill="#2e2f95"/><circle cx="11" cy="9" r="1.5" fill="#fff"/></svg>1280 Harbor Loop Delmont, FL 30210</div>
  </div>
  <nav class="nav"><span class="active">Home</span><span>About</span><span>What We Do</span><span>How We Do It</span><span>Products We Sell</span><span>Contact</span></nav>
  <h1>INTERNATIONAL<br>FLOWER DISTRIBUTOR</h1>
  <p>We Import Farm Fresh Cut Flowers And Send Directly To Supermarkets</p>
  <div class="btn" style="left:502px;top:605px;width:196px;height:40px">Contact Us Today &rsaquo;</div>
</header>

<section class="about">
  <h2 class="section-title" style="top:755px">ABOUT US</h2>
  <div class="divider" style="top:802px"><span></span></div>
  <div class="team-thumb" role="img" aria-label="Portrait of Verna Holt, founder" style="left:198px;background:#d8dadc;outline:4px solid var(--green)"></div>
  <div class="team-thumb" role="img" aria-label="Portrait of Gregory Holt" style="left:363px;background:#7a6e62"></div>
  <div class="team-thumb" role="img" aria-label="Portrait of Danielle Holt" style="left:528px;background:#b89a7e"></div>
  <div class="team-thumb" role="img" aria-label="Portrait of Pilar Wendham" style="left:693px;background:#5a5754"></div>
  <div class="team-thumb" role="img" aria-label="Portrait of Renata Valcourt" style="left:858px;background:#9fa4ab"></div>

  <div class="founder-name">VERNA HOLT <small>(founder)</small></div>
  <p class="lead" style="left:163px;top:1112px;width:436px">Lorem ipsum dolor sit amet, consectetuer adipiscing elit, sed diam nonummy nibh euismod tincidunt.</p>
  <p class="body-copy" style="left:163px;top:1174px;width:436px">Sed ut perspiciatis unde omnis iste natus error sit voluptatem accusantium doloremque laudantium, totam rem aperiam, eaque ipsa quae ab illo inventore veritatis et quasi architecto beatae vitae dicta sunt explicabo. Nemo enim ipsam voluptatem quia voluptas sit aspernatur aut odit aut fugit, sed quia consequuntur magni dolores eos qui ratione voluptatem sequi nesciunt. Neque porro quisquam est, qui dolorem ipsum quia dolor sit amet.</p>
  <div class="socials" style="left:163px;top:1355px" aria-label="Social links"><i></i><i></i><i></i></div>

  <div class="frame-green" style="left:712px;top:1042px;width:338px;height:336px"></div>
  <div class="photo" role="img" aria-label="Portrait of founder Verna Holt" style="left:700px;top:1054px;width:338px;height:338px;background:linear-gradient(135deg,#e8e8e6,#cfcfcb)"></div>
</section>

<section class="what">
  <div class="what-band" role="img" aria-label="Soft blue floral background"></div>
  <h2 class="section-title" style="top:1543px;color:var(--white)">WHAT WE DO</h2>
  <div class="divider" style="top:1588px"><span style="border-color:#dde"></span></div>
  <div class="what-card" role="img" aria-label="Handshake over a business document" style="left:160px;background:linear-gradient(135deg,#e9e4de,#c9bcae)"></div>
  <div class="what-card" role="img" aria-label="Team reviewing orders in a flower greenhouse" style="left:467px;background:linear-gradient(135deg,#cfd7c4,#d9b63e)"></div>
  <div class="what-card" role="img" aria-label="Account team working together at a laptop" style="left:773px;background:linear-gradient(135deg,#7b8694,#c8ccd2)"></div>
  <div class="what-caption" style="left:179px">Personalized Customer<br>Service</div>
  <div class="what-caption" style="left:486px">Exclusively Mass Market<br>Experience To Meet High<br>Demands</div>
  <div class="what-caption" style="left:792px">Dedicated Team Assigned<br>To Your Account</div>
</section>

<section class="how">
  <h2 class="section-title" style="top:2020px">HOW WE DO IT</h2>
  <div class="divider" style="top:2066px"><span></span></div>
  <div class="how-icon" style="left:240px"><svg viewBox="0 0 60 60" fill="none" stroke="#2e2f95" stroke-width="2"><rect x="20" y="6" width="20" height="16"/><path d="M6 40l12-10 10 4 10-4 14 10-12 10-10-6-10 6z"/></svg></div>
  <div class="how-icon" style="left:550px"><svg viewBox="0 0 60 60" fill="none" stroke="#2e2f95" stroke-width="2"><path d="M10 46L48 12M38 14l10-2-2 10M22 24l-10-4M36 38l4 10"/><rect x="30" y="40" width="12" height="10" stroke="#7bc13a"/></svg></div>
  <div class="how-icon" style="left:855px"><svg viewBox="0 0 60 60" fill="none" stroke="#2e2f95" stroke-width="2"><path d="M18 50V26M42 50V26M10 30l8-10 8 10M34 30l8-10 8 10M30 50V34"/><path d="M14 12l4-4M30 8v-4M44 12l4-4" stroke="#7bc13a"/></svg></div>
  <svg class="how-arrow" style="left:378px" viewBox="0 0 140 40"><path d="M4 34Q70-6 130 30" fill="none" stroke="#bbb" stroke-dasharray="3 4"/><path d="M124 24l7 7-9 2" fill="none" stroke="#bbb"/></svg>
  <svg class="how-arrow" style="left:688px" viewBox="0 0 140 40"><path d="M4 10Q70 56 130 10" fill="none" stroke="#bbb" stroke-dasharray="3 4"/><path d="M122 8l8 2-4 8" fill="none" stroke="#bbb"/></svg>
  <p class="how-text" style="left:180px">Partnerships with farms<br>in Colombia, Ecuador and<br>Costa rica</p>
  <p class="how-text" style="left:490px">Farm fresh delivered<br>directly from cargo planes to<br>state of the art cooler facility<br>at Delmont Airport</p>
  <p class="how-text" style="left:793px">Verity Trust</p>
  <div class="btn" style="left:543px;top:2338px;width:114px;height:36px;font-size:13.5px">Contact Us</div>
</section>

<section class="banner" role="region" aria-label="Company statement">
  <div class="photo" role="img" aria-label="Faded photo of a woman with flowers in a field" style="inset:0;border-radius:8px;background:radial-gradient(ellipse at 50% 40%,rgba(190,200,160,.35),rgba(255,255,255,0) 70%)"></div>
  <h2>WE ARE INTERNATIONAL FLOWER DISTRIBUTOR.<br>WE ARE NOT A FLOWER SHOP.</h2>
  <p>Lorem ipsum dolor sit amet, consectetuer adipiscing elit, sed diam nonummy nibh euismod tincidunt ut laoreet dolore magna aliquam erat volutpat. Ut wisi enim ad minim veniam, quis nostrud exerci tation ullamcorper suscipit lobortis nisl ut aliquip ex ea commodo consequat.</p>
  <div class="btn" style="left:380px;top:238px;width:120px;height:36px;font-size:13.5px">Contact Us</div>
</section>

<section class="products">
  <div class="photo" role="img" aria-label="Green tinted flower field background" style="inset:0;background:linear-gradient(180deg,rgba(255,255,255,.06),rgba(0,0,0,0) 40%,rgba(40,80,10,.12))"></div>
  <h2 class="section-title" style="top:70px">PRODUCTS WE SELL</h2>
  <div class="divider" style="top:120px"><span style="border-color:#eef"></span></div>

  <h3 class="prod-title" style="left:163px;top:228px">FARM MADE BOUQUETS</h3>
  <p class="lead" style="left:163px;top:265px;width:436px">Lorem ipsum dolor sit amet, consectetuer adipiscing elit, sed diam nonummy nibh euismod tincidunt.</p>
  <p class="body-copy" style="left:163px;top:328px;width:436px">Sed ut perspiciatis unde omnis iste natus error sit voluptatem accusantium doloremque laudantium, totam rem aperiam, eaque ipsa quae ab illo inventore veritatis et quasi architecto beatae vitae dicta sunt explicabo. Nemo enim ipsam voluptatem quia voluptas sit aspernatur aut odit aut fugit, sed quia consequuntur magni dolores eos qui ratione voluptatem sequi nesciunt.</p>
  <div class="frame-navy" style="left:712px;top:175px;width:338px;height:338px"></div>
  <div class="photo" role="img" aria-label="Wrapped bouquets of pink and yellow roses" style="left:700px;top:187px;width:338px;height:335px;background:linear-gradient(135deg,#e0306e,#e8d25a 50%,#d42a64)"></div>

  <div class="frame-navy" style="left:150px;top:545px;width:336px;height:336px"></div>
  <div class="photo" role="img" aria-label="Buckets of colourful consumer flower bunches" style="left:162px;top:557px;width:336px;height:338px;background:linear-gradient(135deg,#e8c33a,#c04a8a 50%,#3aa0b0)"></div>
  <h3 class="prod-title" style="left:600px;top:612px">CONSUMER BUNCHES</h3>
  <p class="lead" style="left:600px;top:647px;width:436px">Lorem ipsum dolor sit amet, consectetuer adipiscing elit, sed diam nonummy nibh euismod tincidunt.</p>
  <p class="body-copy" style="left:600px;top:710px;width:436px">Sed ut perspiciatis unde omnis iste natus error sit voluptatem accusantium doloremque laudantium, totam rem aperiam, eaque ipsa quae ab illo inventore veritatis et quasi architecto beatae vitae dicta sunt explicabo. Nemo enim ipsam voluptatem quia voluptas sit aspernatur aut odit aut fugit, sed quia consequuntur magni dolores eos qui ratione voluptatem sequi nesciunt.</p>

  <h3 class="prod-title" style="left:163px;top:970px">PROGRAMS TAILORED TO FIT<br>CUSTOMER'S RETAIL PROGRAM</h3>
  <p class="lead" style="left:163px;top:1032px;width:436px">Lorem ipsum dolor sit amet, consectetuer adipiscing elit, sed diam nonummy nibh euismod tincidunt.</p>
  <p class="body-copy" style="left:163px;top:1095px;width:436px">Sed ut perspiciatis unde omnis iste natus error sit voluptatem accusantium doloremque laudantium, totam rem aperiam, eaque ipsa quae ab illo inventore veritatis et quasi architecto beatae vitae dicta sunt explicabo. Nemo enim ipsam voluptatem quia voluptas sit aspernatur aut odit aut fugit, sed quia consequuntur magni dolores eos qui ratione voluptatem sequi nesciunt.</p>
  <div class="frame-navy" style="left:712px;top:915px;width:338px;height:338px"></div>
  <div class="photo" role="img" aria-label="Florist arranging flowers in a retail setting" style="left:700px;top:927px;width:338px;height:335px;background:linear-gradient(135deg,#d8d2c4,#a34a3e 55%,#8a8f7a)"></div>
</section>

<section class="info">
  <h2 class="section-title" style="top:4278px">FOR MORE INFORMATION</h2>
  <div class="divider" style="top:4326px"><span></span></div>

  <div class="contact-name" style="left:390px;top:4398px">GREGORY HOLT</div>
  <div class="contact-role" style="left:402px;top:4432px">Director of Operations</div>
  <div class="contact-row right" style="left:418px;top:4476px"><div>Phone<br>555-310-4420</div><div class="dot"><svg viewBox="0 0 18 18"><rect x="5" y="2" width="8" height="14" rx="1.5" fill="none" stroke="#fff" stroke-width="1.6"/></svg></div></div>
  <div class="contact-row right" style="left:322px;top:4540px"><div>Email<br>gregory@marlowevantage.com</div><div class="dot"><svg viewBox="0 0 18 18"><rect x="2" y="4" width="14" height="10" fill="#fff"/><path d="M2 4l7 6 7-6" fill="none" stroke="#7bc13a" stroke-width="1.4"/></svg></div></div>

  <div class="contact-name" style="left:653px;top:4398px">DANIELLE HOLT</div>
  <div class="contact-role" style="left:653px;top:4432px">Account Executive</div>
  <div class="contact-row" style="left:653px;top:4476px"><div class="dot"><svg viewBox="0 0 18 18"><rect x="5" y="2" width="8" height="14" rx="1.5" fill="none" stroke="#fff" stroke-width="1.6"/></svg></div><div>Phone<br>555-310-4477</div></div>
  <div class="contact-row" style="left:653px;top:4535px"><div class="dot"><svg viewBox="0 0 18 18"><rect x="2" y="4" width="14" height="10" fill="#fff"/><path d="M2 4l7 6 7-6" fill="none" stroke="#7bc13a" stroke-width="1.4"/></svg></div><div>Email<br>danielle@marlowevantage.com</div></div>

  <div class="btn" style="left:518px;top:4627px;width:164px;height:36px;font-size:13.5px">Send Email Inquiry</div>
</section>

<footer class="footer">
  <p>© 2022 Marlowe Vantage Flower Distributors. All Rights Reserved.</p>
  <div class="socials" aria-label="Social links"><i></i><i></i><i></i></div>
</footer>

</body>
</html>
```